App design for Monitoring/Notifying Patient's Medication

Design of UX for an Android App that helps patients with medications.

Patient should be able to interact with the App to inform that they have taken the medication (tablets and injections) at proper times.
Ability in App to notify the patient for taking medicines or injections at the proper times.
Medicines and injections to be taken multiple times a day.
Notifications can be visual and audio. Audio may include name and dosage info also.

App requirements
Ability for patient to interact with app to inform that medicine and/or injection has been taken.
Ability to show visual/audio notifications at scheduled times if patient has not taken medicine or injection.
Audio may contain name and dosage of medicine.
In order to increase the use of App, please suggest how to add a rewards section. High level intent is to reward patients who have been taking medications as prescribed for a month.
Menu button at the top which will have 3 action buttons:
1- Home : on click of which the user is back on the landing/notification page.
2-On click of which this will lead the user to a details screen where he can view his medication details as to what all medicines and injections he is taking along with the schedules and the next upcoming notification. This page is entirely read only. It may have a button to help the user go back to the landing page.
3-On click of which, this will show a history of his actions taken in the last 30 days, if the user has pushed the button on notification every time he has consumed the medicine. This page is entirely read only. It may have a button to help the user go back to the landing page.

Thus 3 screens have to be designed:
Home Page
Page for Menu Action button 2
Page for Menu Action button 3

The menu button should be available in all the 3 pages.

The app needs to be simple, friendly and lively so that it ignites an interest in the user to use the app. Please note that many users are illiterate.

It has to be designed only for android phones that will have around 5 inche screen with a resolution between 360 x 640 and 1280 x 720 pixels

Target Market(s)

Patients(most of them are illiterate

Industry/Entity Type

Healthcare

Requirements
Must have
• - best use of screen space. minimum click and scrolls.
• - clean and elegant look.
• - basic font styles
• - bright colors.

```html
<!DOCTYPE html>
<html lang="en">
<head>
<meta charset="utf-8">
<title>dosely – Splash and Home Screen</title>
<link rel="stylesheet" href="https://fonts.googleapis.com/css2?family=Raleway:ital,wght@0,400;0,500;0,700;1,400&display=swap">
<style>
  :root{
    --stage:#7a8590;
    --title:#8cc0f0;
    --note:#ffffff;
    --rule:#8cbcf0;
    --sky-top:#8dc1f5;
    --sky-bottom:#6296e0;
    --header:#8ec3f5;
    --header-light:#b6d8f8;
    --white:#ffffff;
    --take:#5dd39a;
    --later:#dcdcdc;
    --chevron:#c4c4c4;
    --cell:#ffffff;
    --cell-future:#e2e2e2;
    --hour:#d8d8d8;
    --hour-text:#7b7b7b;
    --missed:#c8c8c8;
    --now:#4d86d8;
    --pill-blue:#5b8fdc;
    --daybar:#555b60;
    --reward:#f26b1d;
  }
  *{margin:0;padding:0;box-sizing:border-box}
  html,body{width:1200px;height:1000px;overflow:hidden}
  body{background:var(--stage);font-family:'Raleway',sans-serif;color:var(--note);position:relative}

  .screen-title{position:absolute;width:400px;text-align:center;font-weight:500;font-size:23px;color:var(--title);top:56px}
  .screen-subtitle{position:absolute;width:400px;text-align:center;font-size:14px;top:83px;color:var(--note)}

  .splash{position:absolute;left:213px;top:205px;width:327px;height:580px;background:linear-gradient(180deg,var(--sky-top),var(--sky-bottom));display:flex;align-items:center;justify-content:center}
  .splash .wordmark{font-weight:700;font-size:64px;color:var(--white);letter-spacing:1px;margin-top:-10px}

  .home{position:absolute;left:661px;top:205px;width:327px;height:580px;overflow:hidden;background:var(--cell)}
  .home .header{position:absolute;left:0;top:0;width:327px;height:265px;background:linear-gradient(135deg,var(--header-light) 0%,var(--header) 35%,var(--header) 100%)}
  .menu-button{position:absolute;left:274px;top:28px;width:25px;height:19px;display:flex;flex-direction:column;justify-content:space-between}
  .menu-button span{display:block;height:3px;background:var(--white);border-radius:1px}
  .medication-badge{position:absolute;left:33px;top:56px;width:114px;height:114px;border-radius:50%;background:var(--white)}
  .medication-badge svg{position:absolute;left:27px;top:36px}
  .due-note{position:absolute;left:159px;top:64px;display:flex;align-items:center;gap:6px;font-size:13px;color:var(--header-light)}
  .drug-name{position:absolute;left:159px;top:100px;font-size:26px;font-weight:500;color:var(--white)}
  .drug-dose{position:absolute;left:159px;top:132px;font-size:13px;line-height:16px;color:var(--white)}

  .swipe-action{position:absolute;left:31px;top:192px;width:266px;height:40px;border-radius:20px;background:var(--white);border:2px solid var(--header-light)}
  .swipe-action .later-track{position:absolute;left:2px;top:2px;width:176px;height:32px;border-radius:16px;background:var(--later)}
  .swipe-action .later-label{position:absolute;left:15px;top:7px;font-size:18px;color:var(--white)}
  .swipe-action .take-knob{position:absolute;left:93px;top:2px;width:79px;height:32px;border-radius:16px;background:var(--take);color:var(--white);font-weight:700;font-size:18px;display:flex;align-items:center;justify-content:center;gap:6px}
  .swipe-action .hint{position:absolute;top:7px;font-size:16px;font-weight:700;color:var(--chevron)}

  .schedule{position:absolute;left:0;top:265px}

  .label-right{position:absolute;left:1043px;font-size:12px;line-height:14.5px}
  .label-right b{font-weight:700}
  .label-right i{font-style:italic}
  .rule-v{position:absolute;width:1px;background:var(--rule)}
  .rule-h{position:absolute;height:1px;background:var(--rule)}
  .label-side{position:absolute;font-size:12px;transform:rotate(-90deg);transform-origin:left top;white-space:nowrap}
  .label-bottom{position:absolute;font-size:12px;text-align:center}
</style>
</head>
<body>

  <div class="screen-title" style="left:171px">Splash Screen</div>
  <div class="screen-subtitle" style="left:171px">Branding (Name and Logo)</div>
  <div class="screen-title" style="left:620px">Home Screen</div>
  <div class="screen-subtitle" style="left:620px">Notification, History / Schedule, Rewards</div>

  <section class="splash">
    <div class="wordmark">dosely</div>
  </section>

  <section class="home">
    <div class="header">
      <div class="menu-button"><span></span><span></span><span></span></div>
      <div class="medication-badge">
        <svg width="60" height="40" viewBox="0 0 60 40">
          <ellipse cx="30" cy="24" rx="29" ry="14" fill="#4a7cc8"/>
          <ellipse cx="30" cy="18" rx="29" ry="14" fill="var(--pill-blue)"/>
          <line x1="27" y1="9" x2="33" y2="22" stroke="#fff" stroke-width="3" stroke-linecap="round"/>
        </svg>
      </div>
      <div class="due-note">
        <svg width="26" height="30" viewBox="0 0 26 30" fill="none" stroke="var(--header-light)" stroke-width="2.4">
          <circle cx="13" cy="17" r="11"/><line x1="9" y1="2" x2="17" y2="2"/><line x1="13" y1="2" x2="13" y2="6"/><polyline points="13,10 13,17 17,17"/>
        </svg>
        <span>It is time to take</span>
      </div>
      <div class="drug-name">Rifampicin</div>
      <div class="drug-dose">1 Filmtablette<br>15 mg</div>
      <div class="swipe-action">
        <div class="later-track"></div>
        <div class="later-label">later</div>
        <div class="take-knob">take <span>›</span></div>
        <div class="hint" style="left:176px">›</div>
        <div class="hint" style="left:196px">›</div>
      </div>
    </div>

    <svg class="schedule" width="327" height="315" viewBox="0 0 327 315">
      <defs>
        <symbol id="capsule" viewBox="0 0 48 14"><rect x="0" y="0" width="48" height="14" rx="7"/><line x1="24" y1="0" x2="24" y2="14" stroke="rgba(0,0,0,0.12)" stroke-width="2"/></symbol>
        <symbol id="tablet" viewBox="0 0 34 20"><ellipse cx="17" cy="12" rx="16" ry="7" opacity="0.8"/><ellipse cx="17" cy="9" rx="16" ry="7"/><line x1="15" y1="4" x2="19" y2="11" stroke="#fff" stroke-width="2" stroke-linecap="round"/></symbol>
        <symbol id="syringe" viewBox="0 0 56 16"><rect x="0" y="3" width="3" height="10"/><rect x="4" y="6" width="4" height="4"/><rect x="8" y="1" width="28" height="14" rx="5"/><rect x="36" y="6" width="4" height="4"/><rect x="40" y="7" width="16" height="2" rx="1"/><g stroke="#fff" stroke-width="1.5"><line x1="14" y1="5" x2="14" y2="11"/><line x1="19" y1="5" x2="19" y2="11"/><line x1="24" y1="5" x2="24" y2="11"/></g></symbol>
      </defs>

      <rect x="0" y="0" width="327" height="275" fill="#ffffff"/>
      <rect x="0" y="0" width="17" height="275" fill="var(--hour)"/>
      <rect x="165" y="0" width="162" height="275" fill="var(--cell-future)"/>
      <g stroke="#ffffff" stroke-width="3">
        <line x1="163.5" y1="0" x2="163.5" y2="275"/><line x1="236.5" y1="0" x2="236.5" y2="275"/><line x1="309.5" y1="0" x2="309.5" y2="275"/>
      </g>
      <g stroke="var(--hour)" stroke-width="2">
        <line x1="90.5" y1="0" x2="90.5" y2="275"/>
      </g>
      <g stroke="#ffffff" stroke-width="2">
        <line x1="17" y1="30.5" x2="327" y2="30.5"/><line x1="17" y1="61" x2="327" y2="61"/><line x1="17" y1="91.5" x2="327" y2="91.5"/><line x1="17" y1="122" x2="327" y2="122"/><line x1="17" y1="152.5" x2="327" y2="152.5"/><line x1="17" y1="183" x2="327" y2="183"/><line x1="17" y1="213.5" x2="327" y2="213.5"/><line x1="17" y1="244" x2="327" y2="244"/>
      </g>
      <g stroke="var(--hour)" stroke-width="1.5">
        <line x1="17" y1="30.5" x2="163" y2="30.5"/><line x1="17" y1="61" x2="163" y2="61"/><line x1="17" y1="91.5" x2="163" y2="91.5"/><line x1="17" y1="122" x2="163" y2="122"/><line x1="17" y1="152.5" x2="163" y2="152.5"/><line x1="17" y1="183" x2="163" y2="183"/><line x1="17" y1="213.5" x2="163" y2="213.5"/><line x1="17" y1="244" x2="163" y2="244"/>
      </g>
      <g fill="var(--hour-text)" font-family="Raleway, sans-serif" font-size="8" font-weight="700" text-anchor="middle">
        <text x="8.5" y="17">6</text><text x="8.5" y="48">8</text><text x="8.5" y="78">10</text><text x="8.5" y="109">12</text><text x="8.5" y="139">14</text><text x="8.5" y="170">16</text><text x="8.5" y="200">18</text><text x="8.5" y="231">20</text><text x="8.5" y="261">22</text>
      </g>

      <polygon points="188,0 212,0 200,14" fill="var(--header)"/>
      <rect x="165" y="62" width="70" height="29" fill="var(--now)"/>

      <!-- 8:00 -->
      <use href="#capsule" x="30" y="38" width="48" height="14" fill="var(--take)"/>
      <use href="#capsule" x="103" y="38" width="48" height="14" fill="var(--take)"/>
      <use href="#capsule" x="176" y="38" width="48" height="14" fill="var(--take)"/>
      <use href="#capsule" x="249" y="38" width="48" height="14" fill="#fff"/>
      <use href="#capsule" x="316" y="38" width="48" height="14" fill="#fff"/>
      <!-- 10:00 -->
      <use href="#tablet" x="37" y="66" width="34" height="20" fill="var(--take)"/>
      <use href="#tablet" x="110" y="66" width="34" height="20" fill="var(--take)"/>
      <use href="#tablet" x="183" y="66" width="34" height="20" fill="#fff"/>
      <use href="#tablet" x="256" y="66" width="34" height="20" fill="#fff"/>
      <use href="#tablet" x="318" y="66" width="34" height="20" fill="#fff"/>
      <!-- 12:00 -->
      <use href="#syringe" x="26" y="98" width="56" height="16" fill="var(--take)"/>
      <use href="#tablet" x="110" y="96" width="34" height="20" fill="var(--take)"/>
      <use href="#syringe" x="172" y="98" width="56" height="16" fill="#fff"/>
      <use href="#tablet" x="256" y="96" width="34" height="20" fill="#fff"/>
      <use href="#syringe" x="316" y="98" width="56" height="16" fill="#fff"/>
      <!-- 18:00 -->
      <use href="#capsule" x="30" y="191" width="48" height="14" fill="var(--take)"/>
      <use href="#capsule" x="103" y="191" width="48" height="14" fill="var(--missed)"/>
      <use href="#capsule" x="176" y="191" width="48" height="14" fill="#fff"/>
      <use href="#capsule" x="249" y="191" width="48" height="14" fill="#fff"/>
      <use href="#capsule" x="316" y="191" width="48" height="14" fill="#fff"/>
      <!-- 20:00 -->
      <use href="#capsule" x="30" y="221" width="48" height="14" fill="var(--take)"/>
      <use href="#capsule" x="103" y="221" width="48" height="14" fill="var(--take)"/>
      <use href="#capsule" x="176" y="221" width="48" height="14" fill="#fff"/>
      <use href="#capsule" x="249" y="221" width="48" height="14" fill="#fff"/>
      <use href="#capsule" x="316" y="221" width="48" height="14" fill="#fff"/>

      <!-- day bar -->
      <rect x="0" y="275" width="327" height="40" fill="var(--daybar)"/>
      <rect x="0" y="275" width="17" height="40" fill="#8a9096"/>
      <g stroke="#8a9096" stroke-width="3">
        <line x1="90.5" y1="275" x2="90.5" y2="315"/><line x1="163.5" y1="275" x2="163.5" y2="315"/><line x1="236.5" y1="275" x2="236.5" y2="315"/><line x1="309.5" y1="275" x2="309.5" y2="315"/>
      </g>
      <g fill="#ffffff" font-family="Raleway, sans-serif" text-anchor="middle">
        <text x="54" y="305" font-size="9">Mar 14</text>
        <text x="127" y="293" font-size="14" font-weight="700">Tue</text><text x="127" y="305" font-size="9">Mar 15</text>
        <text x="200" y="293" font-size="14" font-weight="700">Fri</text><text x="200" y="305" font-size="9">Mar 16</text>
        <text x="273" y="293" font-size="14" font-weight="700">Sat</text><text x="273" y="305" font-size="9">Mar 17</text>
      </g>

      <!-- reward badge -->
      <g stroke="var(--reward)" stroke-width="2" stroke-linecap="round">
        <line x1="55" y1="248" x2="55" y2="242"/><line x1="44" y1="251" x2="40" y2="246"/><line x1="66" y1="251" x2="70" y2="246"/>
        <line x1="36" y1="258" x2="30" y2="255"/><line x1="74" y1="258" x2="80" y2="255"/><line x1="33" y1="267" x2="27" y2="267"/><line x1="77" y1="267" x2="83" y2="267"/>
      </g>
      <circle cx="55" cy="272" r="18" fill="var(--reward)"/>
      <polygon points="55,261 58,268.5 66,269 60,274 62,282 55,277.5 48,282 50,274 44,269 52,268.5" fill="#ffffff"/>
    </svg>
  </section>

  <!-- annotations right -->
  <div class="rule-v" style="left:1033px;top:233px;height:17px"></div>
  <div class="label-right" style="top:233px"><b>Menu</b></div>
  <div class="rule-v" style="left:1033px;top:260px;height:118px"></div>
  <div class="label-right" style="top:259px"><b>Notification Details</b><br>Time<br>Name<br>Dosage</div>
  <div class="rule-v" style="left:1033px;top:395px;height:45px"></div>
  <div class="label-right" style="top:394px"><b>Notification Action</b><br><i>Swipe right</i> if take now<br><i>Swipe left</i> if take later</div>
  <div class="rule-v" style="left:1033px;top:470px;height:275px"></div>
  <div class="label-right" style="top:470px"><b>Medication Schedule</b><br>History of actions<br>Upcoming notifications</div>

  <!-- annotations left -->
  <div class="rule-v" style="left:616px;top:262px;height:116px"></div>
  <div class="label-side" style="left:597px;top:365px">Medication type</div>
  <div class="rule-v" style="left:616px;top:470px;height:275px"></div>
  <div class="label-side" style="left:597px;top:654px">Hours of the day</div>

  <!-- annotations bottom -->
  <div class="label-bottom" style="left:680px;top:866px;width:76px">Reward</div>
  <div class="rule-h" style="left:680px;top:886px;width:72px"></div>
  <div class="label-bottom" style="left:661px;top:894px;width:161px">Past days</div>
  <div class="rule-h" style="left:661px;top:913px;width:161px"></div>
  <div class="label-bottom" style="left:826px;top:894px;width:70px">Today</div>
  <div class="rule-h" style="left:826px;top:913px;width:70px"></div>
  <div class="label-bottom" style="left:899px;top:894px;width:89px">Tomorrow</div>
  <div class="rule-h" style="left:899px;top:913px;width:89px"></div>

</body>
</html>
```